Hypothetical Customer Lifecycle

Need a poster to show the lifecycle of a student going through university.

There are three main stages of the lifecycle, it also needs to visually loop back in some way to the start from the end of the 3rd stage.

1) Prospect – Strategy is to Acquire
There are three main sub experiences within this stage which are
a. Decide
b. Apply
c. On board
Within the Prospect stage we also need to show some Needs and Pain Points as below
Needs
• Validation on choices from peers or family
• Clear direction on choices
Pain Points
• Not sure where to start
• Poor navigation and information architecture

2) Current – Strategy is to Engage
a. Commence
b. Study
c. Complete
Within the Current stage we also need to show some Needs and Pain Points as below
Needs
• Access to peer groups and faculty
• Flexibility in modes of learning
Pain Points
• Quality of faculty engagement can vary
• Online tools are hard to use

3) Alumni – Strategy is to Retain
a. Graduate
b. Job Seek
c. Network
Needs
• Options to further career
• Competency based learning
Pain Points
• Lots of irrelevant emails and mail
• Struggle to relate to Alumni programs

Target Market(s)

Exec level, technology managers

Industry/Entity Type

Education

Font styles to use
Sans Serif

Colors
1696d0
ecf7fb
3176b5
ffffff

Requirements
Must have
• Simple visual elements
Should not have
• Try and avoid arrows, chevrons anything that strongly implies a process.

```html
<!DOCTYPE html>
<html lang="en">
<head>
<meta charset="utf-8">
<title>Hypothetical Customer Lifecycle</title>
<link href="https://fonts.googleapis.com/css2?family=Arvo:wght@700&family=Lato:wght@400;700&family=Oswald:wght@500&display=swap" rel="stylesheet">
<style>
:root{
  --brand:#1696d0;
  --pale:#ecf7fb;
  --mid:#3176b5;
  --white:#ffffff;
  --navy:#1f4f86;
  --deep:#1c4f8a;
  --sky:#7fc0f7;
  --sky-soft:#a8d5fb;
  --ink:#17406f;
}
*{box-sizing:border-box;margin:0;padding:0}
html,body{width:1200px;height:1000px;overflow:hidden;background:var(--pale)}
.poster{position:relative;width:1200px;height:1000px;overflow:hidden;font-family:"Lato",sans-serif}
.stage{position:absolute;top:0;height:1000px}
.stage--prospect{left:0;width:397px;background:radial-gradient(circle at 196px 560px,#d6ecff 0,var(--sky) 60%,#6db3f0 100%)}
.stage--current{left:397px;width:401px;background:radial-gradient(circle at 200px 560px,#5a9ede 0,var(--mid) 65%,#2a69a6 100%)}
.stage--alumni{left:798px;width:402px;background:radial-gradient(circle at 200px 560px,#3a7fc2 0,#225f9e 65%,var(--deep) 100%)}
.stage__art{position:absolute;left:0;top:0}
.title-banner{position:absolute;left:0;top:0;width:1200px;height:130px}
.title-banner__text{position:absolute;left:0;right:0;top:50px;text-align:center;font-family:"Arvo",serif;font-size:40px;color:var(--white);letter-spacing:.5px}
.stage-head{position:absolute;top:166px;display:flex;align-items:center;gap:12px}
.stage-head__num{width:42px;height:42px;border-radius:50%;background:var(--white);color:var(--mid);font-family:"Arvo",serif;font-size:24px;display:flex;align-items:center;justify-content:center}
.stage-head__name{font-family:"Arvo",serif;font-size:27px;color:var(--white)}
.strategy{position:absolute;top:226px;height:56px;background:var(--white);border-top:2px dashed var(--mid);border-bottom:2px dashed var(--mid);display:flex;align-items:center;justify-content:center;font-size:21px;font-weight:700;color:var(--navy)}
.strategy--left{left:0;width:250px;clip-path:polygon(0 0,96% 0,100% 50%,96% 100%,0 100%)}
.strategy--center{left:70px;width:268px;clip-path:polygon(4% 0,96% 0,100% 50%,96% 100%,4% 100%,0 50%)}
.strategy--right{right:0;width:276px;clip-path:polygon(4% 0,100% 0,100% 100%,4% 100%,0 50%)}
.figure{position:absolute;top:380px;width:132px;height:436px;border-radius:60px 60px 14px 14px}
.figure--prospect{left:130px;background:linear-gradient(#2b2b2b 0,#f2cfa8 18%,#c93a3a 40%,#133e7a 70%)}
.figure--current{left:140px;background:linear-gradient(#c99a4a 0,#f2cfa8 22%,#2f7ad8 42%,#2a3040 75%)}
.figure--alumni{left:134px;background:linear-gradient(#2d2d2d 0,#f5b940 16%,#f2cfa8 24%,#222 42%)}
.badge{position:absolute;width:108px;height:108px;margin:-54px 0 0 -54px;border-radius:50%;background:var(--white);border:5px solid var(--deep);display:flex;flex-direction:column;align-items:center;justify-content:center;gap:2px}
.badge svg{width:46px;height:40px}
.badge__label{font-family:"Oswald",sans-serif;font-size:19px;color:var(--deep);line-height:1}
.notes{position:absolute;top:852px;left:26px;right:10px;display:grid;grid-template-columns:1fr 1fr;gap:14px}
.notes__head{display:flex;align-items:center;gap:10px;height:46px}
.notes__icon{width:40px;height:40px;border-radius:50%;background:var(--white);display:flex;align-items:center;justify-content:center}
.notes__icon svg{width:26px;height:26px}
.notes__title{font-family:"Arvo",serif;font-size:21px;line-height:.95;color:var(--white)}
.notes ul{list-style:none;margin-top:12px}
.notes li{font-size:13.5px;line-height:18px;color:var(--white);padding-left:10px;text-indent:-10px}
.notes li::before{content:"• "}
.stage--prospect .notes__title{color:var(--navy)}
.stage--prospect .notes li{color:var(--ink)}
</style>
</head>
<body>
<main class="poster">

  <section class="stage stage--prospect">
    <svg class="stage__art" width="397" height="1000" viewBox="0 0 397 1000">
      <g fill="none" stroke="#3d6ea8" stroke-width="1" opacity=".5">
        <circle cx="196" cy="560" r="70"/><circle cx="196" cy="560" r="125"/><circle cx="196" cy="560" r="180"/>
      </g>
      <polygon points="0,650 94,650 94,618 150,724 94,830 94,800 0,800" fill="#1f5a9a"/>
    </svg>
    <div class="stage-head" style="left:80px"><span class="stage-head__num">1</span><span class="stage-head__name">PROSPECT</span></div>
    <div class="strategy strategy--left">Strategy is to Acquire</div>
    <div class="figure figure--prospect" role="img" aria-label="Illustrated prospective student holding a brochure"></div>
    <div class="badge" style="left:76px;top:425px">
      <svg viewBox="0 0 46 40"><rect x="21" y="2" width="4" height="36" fill="#1c4f8a"/><polygon points="8,8 36,8 40,13 36,18 8,18" fill="#1c4f8a"/><polygon points="10,22 38,22 38,32 10,32 6,27" fill="#1c4f8a"/></svg>
      <span class="badge__label">DECIDE</span></div>
    <div class="badge" style="left:290px;top:374px">
      <svg viewBox="0 0 46 40"><rect x="6" y="4" width="28" height="28" fill="none" stroke="#1c4f8a" stroke-width="3" stroke-dasharray="7 5"/><polygon points="26,18 40,30 33,31 37,38 34,39 30,33 26,37" fill="#1c4f8a"/></svg>
      <span class="badge__label">APPLY</span></div>
    <div class="badge" style="left:324px;top:610px">
      <svg viewBox="0 0 46 40"><rect x="2" y="4" width="16" height="14" fill="#1c4f8a"/><rect x="28" y="4" width="16" height="14" fill="#1c4f8a"/><path d="M6 30h12M14 26l4 4-4 4M40 30H28M32 26l-4 4 4 4" stroke="#3176b5" stroke-width="3" fill="none"/></svg>
      <span class="badge__label">ON BOARD</span></div>
    <div class="notes">
      <div>
        <div class="notes__head"><span class="notes__icon"><svg viewBox="0 0 26 26"><circle cx="14" cy="10" r="7" fill="#3176b5"/><path d="M2 20h8l6 2 8-4v3l-8 4H2z" fill="#1c4f8a"/></svg></span><span class="notes__title">NEEDS</span></div>
        <ul><li>Validation on choices from peers or family</li><li>Clear direction on choices</li></ul>
      </div>
      <div>
        <div class="notes__head"><span class="notes__icon"><svg viewBox="0 0 26 26"><g stroke="#3176b5" stroke-width="2.5"><path d="M13 2v7M13 17v7M2 13h7M17 13h7M5 5l5 5M16 16l5 5"/></g></svg></span><span class="notes__title">PAIN<br>POINTS</span></div>
        <ul><li>Not sure where to start</li><li>Poor navigation and information architecture</li></ul>
      </div>
    </div>
  </section>

  <section class="stage stage--current">
    <svg class="stage__art" width="401" height="1000" viewBox="0 0 401 1000">
      <g fill="none" stroke="#9cc8f0" stroke-width="1" opacity=".45">
        <circle cx="200" cy="560" r="70"/><circle cx="200" cy="560" r="125"/><circle cx="200" cy="560" r="180"/>
      </g>
      <polygon points="0,650 90,650 90,618 146,724 90,830 90,800 0,800" fill="#9fd0fa"/>
    </svg>
    <div class="stage-head" style="left:112px"><span class="stage-head__num">2</span><span class="stage-head__name">CURRENT</span></div>
    <div class="strategy strategy--center">Strategy is to Engage</div>
    <div class="figure figure--current" role="img" aria-label="Illustrated current student in a blue top"></div>
    <div class="badge" style="left:90px;top:443px">
      <svg viewBox="0 0 46 40"><polygon points="14,4 40,14 30,32 6,22" fill="none" stroke="#1c4f8a" stroke-width="3"/><rect x="6" y="30" width="36" height="5" fill="#1c4f8a"/><path d="M4 8v10M1 14l3 4 3-4" stroke="#1c4f8a" stroke-width="2.5" fill="none"/></svg>
      <span class="badge__label">COMMENCE</span></div>
    <div class="badge" style="left:320px;top:374px">
      <svg viewBox="0 0 46 40"><circle cx="20" cy="20" r="12" fill="none" stroke="#1c4f8a" stroke-width="3"/><path d="M13 19l6 6 14-20" stroke="#3176b5" stroke-width="3.5" fill="none"/><path d="M29 29l10 9" stroke="#1c4f8a" stroke-width="5"/></svg>
      <span class="badge__label">STUDY</span></div>
    <div class="badge" style="left:332px;top:610px">
      <svg viewBox="0 0 46 40"><path d="M6 18h8v18H6zM16 18l8-14c3 0 5 2 4 6l-2 8h10c3 0 4 3 3 5l-3 11c-1 2-2 2-4 2H16z" fill="#1c4f8a"/></svg>
      <span class="badge__label">COMPLETE</span></div>
    <div class="notes">
      <div>
        <div class="notes__head"><span class="notes__icon"><svg viewBox="0 0 26 26"><circle cx="14" cy="10" r="7" fill="#3176b5"/><path d="M2 20h8l6 2 8-4v3l-8 4H2z" fill="#1c4f8a"/></svg></span><span class="notes__title">NEEDS</span></div>
        <ul><li>Access to peer groups and faculty</li><li>Flexibility in modes of learning</li></ul>
      </div>
      <div>
        <div class="notes__head"><span class="notes__icon"><svg viewBox="0 0 26 26"><g stroke="#3176b5" stroke-width="2.5"><path d="M13 2v7M13 17v7M2 13h7M17 13h7M5 5l5 5M16 16l5 5"/></g></svg></span><span class="notes__title">PAIN<br>POINTS</span></div>
        <ul><li>Quality of faculty engagement can vary</li><li>Online tools are hard to use</li></ul>
      </div>
    </div>
  </section>

  <section class="stage stage--alumni">
    <svg class="stage__art" width="402" height="1000" viewBox="0 0 402 1000">
      <g fill="none" stroke="#8dbde8" stroke-width="1" opacity=".4">
        <circle cx="200" cy="560" r="70"/><circle cx="200" cy="560" r="125"/><circle cx="200" cy="560" r="180"/>
      </g>
      <polygon points="0,650 90,650 90,618 146,724 90,830 90,800 0,800" fill="#3d86c9"/>
    </svg>
    <div class="stage-head" style="left:190px"><span class="stage-head__num">3</span><span class="stage-head__name">ALUMNI</span></div>
    <div class="strategy strategy--right">Strategy is to Retain</div>
    <div class="figure figure--alumni" role="img" aria-label="Illustrated graduate in cap and gown holding a diploma"></div>
    <div class="badge" style="left:77px;top:455px">
      <svg viewBox="0 0 46 40"><polygon points="23,6 44,15 23,24 2,15" fill="#1c4f8a"/><path d="M11 20v9c6 5 18 5 24 0v-9l-12 5z" fill="#1c4f8a"/><path d="M40 17v13" stroke="#1c4f8a" stroke-width="2"/></svg>
      <span class="badge__label">GRADUATE</span></div>
    <div class="badge" style="left:328px;top:374px">
      <svg viewBox="0 0 46 40"><path d="M2 14l10-8 8 6-10 10z" fill="#1c4f8a"/><path d="M44 14l-10-8-8 6 10 10z" fill="#1c4f8a"/><path d="M12 18l10 12c2 2 4 2 6 0l8-8-10-8-6 4z" fill="#3176b5"/></svg>
      <span class="badge__label">JOB SEEK</span></div>
    <div class="badge" style="left:323px;top:610px">
      <svg viewBox="0 0 46 40"><g stroke="#1c4f8a" stroke-width="2"><path d="M23 20L10 8M23 20l14-12M23 20L8 28M23 20l15 8M23 20v16"/></g><circle cx="23" cy="20" r="6" fill="#3176b5"/><g fill="#1c4f8a"><circle cx="10" cy="8" r="4"/><circle cx="37" cy="8" r="4"/><circle cx="8" cy="28" r="4"/><circle cx="38" cy="28" r="4"/><circle cx="23" cy="36" r="3"/></g></svg>
      <span class="badge__label">NETWORK</span></div>
    <div class="notes">
      <div>
        <div class="notes__head"><span class="notes__icon"><svg viewBox="0 0 26 26"><circle cx="14" cy="10" r="7" fill="#3176b5"/><path d="M2 20h8l6 2 8-4v3l-8 4H2z" fill="#1c4f8a"/></svg></span><span class="notes__title">NEEDS</span></div>
        <ul><li>Options to further career</li><li>Competency based learning</li></ul>
      </div>
      <div>
        <div class="notes__head"><span class="notes__icon"><svg viewBox="0 0 26 26"><g stroke="#3176b5" stroke-width="2.5"><path d="M13 2v7M13 17v7M2 13h7M17 13h7M5 5l5 5M16 16l5 5"/></g></svg></span><span class="notes__title">PAIN<br>POINTS</span></div>
        <ul><li>Lots of irrelevant emails and mail</li><li>Struggle to relate to Alumni programs</li></ul>
      </div>
    </div>
  </section>

  <header class="title-banner">
    <svg width="1200" height="130" viewBox="0 0 1200 130">
      <polygon points="190,0 1010,0 1010,130 190,130" fill="#2274b8"/>
      <polygon points="130,50 230,50 230,118 130,118 160,84" fill="#1681c6"/>
      <polygon points="1070,50 970,50 970,118 1070,118 1040,84" fill="#1681c6"/>
      <polygon points="200,0 1000,0 1000,112 200,112" fill="var(--brand)"/>
      <rect x="222" y="14" width="756" height="14" fill="#2a7cc2"/>
      <rect x="222" y="40" width="756" height="2" fill="var(--white)"/>
      <rect x="222" y="103" width="756" height="2" fill="var(--white)"/>
      <polygon points="600,14 623,23 600,32 577,23" fill="var(--white)"/>
    </svg>
    <h1 class="title-banner__text">HYPOTHETICAL CUSTOMER LIFECYCLE</h1>
  </header>

</main>
</body>
</html>
```